Innovative Healthcare Technology Company needs a Business Card Design

We are in need of an innovative business card design for a new healthcare software company called "Lumenwise Data Partners". We develop software that creates medical assessment applications and mobile e-learning prevention services to reduce risk behaviors in adolescent and young adults. Our initial product, the "KESTREL App", conducts a tailored sexual risk assessment and provides a doctor with an insightful patient report to improve sexual risk counseling and ultimately reduce unintended pregnancy, STDs, etc.

We would like the design to incorporate our logo and branding colors (attached) in an innovative and creative manner. The final design should communicate professionalism and healthcare innovation. Our tag line is "prevention is the solution" (doesn't necessarily need to be included) and our target audience is doctors, medical directors, and medical business administrators. Please visit our website for additional info ourbrightmarq.com. Be creative and we look forward to seeing your designs!

Target Market(s)

healthcare - doctors, medical directors and medical business administrators

Industry/Entity Type

Healthcare

Contact Information for Business Card

We would like the design to incorporate our logo and branding colors (attached) in an innovative and creative manner. The final design should communicate professionalism and healthcare innovation. Our tag line is "prevention is the solution" (doesn't necessarily need to be included)

Font styles to use
Other font styles liked:
• quicksand

Requirements
Must have
• our logo and brand colors
• Name, (Mara Feldhovenik, PhD)
• Email (drmara@ourbrightmarq.com)
• phone (555.283.9170)
• Website (ourbrightmarq.com)
Should not have
• cartoon look

```html
<!DOCTYPE html>
<html lang="en">
<head>
<meta charset="utf-8">
<title>Lumenwise Data Partners — Business Card</title>
<link rel="stylesheet" href="https://fonts.googleapis.com/css2?family=Quicksand:wght@300;400;500;600;700&display=swap">
<style>
  :root {
    --backdrop: #2b2b2d;
    --lilac: #9d8faa;
    --plum: #5b2f53;
    --plum-deep: #5a2650;
    --mist: #c2c5c9;
    --navy: #2d4b7e;
    --mark-tile: #857592;
    --ink-plum: #4a2443;
    --white: #ffffff;
    --muted: #9b8ea3;
    --muted-soft: #86758a;
  }
  * { box-sizing: border-box; margin: 0; padding: 0; }
  html, body {
    width: 1200px; height: 1008px; overflow: hidden;
    background: var(--backdrop);
    font-family: "Quicksand", sans-serif;
  }
  .canvas { position: relative; width: 1200px; height: 1008px; }

  .card {
    position: absolute;
    box-shadow: 0 2px 6px rgba(0,0,0,0.35);
    overflow: hidden;
  }

  /* Front */
  .card-front { left: 171px; top: 243px; width: 322px; height: 503px; }
  .front-brand-band {
    height: 239px; background: var(--lilac);
    display: flex; align-items: center; padding: 0 18px;
    gap: 12px;
  }
  .brand-square { width: 20px; height: 20px; background: var(--ink-plum); flex: none; }
  .brand-name { color: var(--ink-plum); font-weight: 500; line-height: 1.05; }
  .brand-name .line-main { display: block; font-size: 31px; }
  .brand-name .line-sub { display: block; font-size: 17px; letter-spacing: 0.5px; }
  .front-plum-band { height: 150px; background: var(--plum); }
  .front-tagline-band {
    height: 114px; background: var(--mist);
    display: flex; justify-content: center; padding-top: 37px;
  }
  .tagline {
    color: var(--navy); font-style: italic; font-weight: 600;
    font-size: 15px; letter-spacing: 0.3px;
  }

  /* Back */
  .card-back {
    left: 727px; top: 240px; width: 319px; height: 506px;
    background: var(--plum-deep); text-align: center;
  }
  .mark-tile {
    position: absolute; left: 89px; top: 49px;
    width: 136px; height: 120px; border-radius: 3px;
    background: var(--mark-tile);
  }
  .holder-name {
    position: absolute; left: 0; right: 0; top: 195px;
    color: var(--white); font-weight: 700; font-size: 23px;
    line-height: 32px; letter-spacing: 1px;
  }
  .contact { position: absolute; left: 0; right: 0; white-space: nowrap; }
  .contact-email { top: 315px; font-size: 16px; font-weight: 300; color: var(--muted-soft); letter-spacing: 1.1px; }
  .contact-phone { top: 365px; font-size: 20px; font-weight: 700; color: var(--muted); letter-spacing: 1.6px; }
  .contact-web { top: 407px; font-size: 19px; font-weight: 700; color: var(--muted); letter-spacing: 1.2px; }
</style>
</head>
<body>
<main class="canvas">
  <section class="card card-front" aria-label="Card front">
    <div class="front-brand-band">
      <span class="brand-square"></span>
      <div class="brand-name">
        <span class="line-main">Lumenwise</span>
        <span class="line-sub">Data Partners</span>
      </div>
    </div>
    <div class="front-plum-band"></div>
    <div class="front-tagline-band">
      <p class="tagline">CLARITY BEFORE THE CLINIC</p>
    </div>
  </section>

  <section class="card card-back" aria-label="Card back">
    <div class="mark-tile"></div>
    <h1 class="holder-name">Mara<br>Feldhovenik, PhD</h1>
    <p class="contact contact-email">drmara@ourbrightmarq.com</p>
    <p class="contact contact-phone">555.283.9170</p>
    <p class="contact contact-web">ourbrightmarq.com</p>
  </section>
</main>
</body>
</html>
```